modern design for software startup

We need a website design. We are a software company developing a cruise management system for cruise ships. We don't want or need something elaborate. In fact, we don't want to show specifics of our products because they are under development and we do not want our competitors to know too much. We want to focus on ideals and principals of our company and hint at what we are doing.

Target Market(s)

cruise lines

Industry/Entity Type

Software

Coding

Coded - Design and coding required

Number of Pages Required

1 page

Font styles to use
Sans Serif

Colors
7f7f7f
5c5c5c

Requirements
Must have
• background pictures of cruise ships, ports, ocean, some developers working on computers in brown and white and fuzzy. can't show specific cruise lines. magazine like style. white text. links at bottom to facebook, twitter, instagram
• email link for investor/partner inquiries.
Nice to have
• Some inspirational quotes here and there. Not overpowering but subtle. content to be provided in text file.
• color schemes - we like the scheme in www.tindelmarsh.com
• doesnt have to be exact but similar is good.

```html
<!DOCTYPE html>
<html lang="en">
<head>
<meta charset="utf-8">
<title>Keelwise Software</title>
<link rel="stylesheet" href="https://fonts.googleapis.com/css2?family=Jura:wght@400;500&family=PT+Sans:wght@400;700&display=swap">
<style>
:root{
  --blue:#0b5aa5;
  --sky:#1aa3e0;
  --navy:#0d2a52;
  --ink:#2b2b2b;
  --grey:#5c5c5c;
  --grey-light:#7f7f7f;
  --footer:#132230;
  --white:#ffffff;
}
*{margin:0;padding:0;box-sizing:border-box}
html,body{width:1200px;height:2740px;overflow:hidden}
body{position:relative;background:var(--white);font-family:"PT Sans",sans-serif;color:var(--grey)}
.abs{position:absolute}
a{color:inherit;text-decoration:none}
.heading{font-family:"Jura",sans-serif;font-weight:500;text-align:center;font-size:48px;letter-spacing:.5px}
.heading .accent{color:var(--blue)}

/* hero */
.hero-art{left:0;top:0;width:1200px;height:760px}
.brand{left:78px;top:80px;display:flex;align-items:center;gap:12px}
.brand-mark{width:36px;height:36px;border-radius:50%;background:var(--blue)}
.brand-name{font-weight:700;font-size:26px;color:var(--blue);letter-spacing:1px}
.main-nav{left:374px;top:42px;display:flex}
.main-nav a{font-size:19px;color:var(--white);text-transform:uppercase;padding:0 28px}
.main-nav a.current{color:var(--navy)}
.tagline{right:80px;top:206px;width:560px;text-align:right;color:var(--white);font-size:25px;line-height:36px}
.btn-light{left:913px;top:305px;width:208px;height:51px;background:var(--white);color:var(--ink);font-size:21px;display:flex;align-items:center;justify-content:center;text-transform:uppercase}

/* welcome */
.welcome-title{left:0;width:1200px;top:775px;color:var(--sky)}
.welcome-text{left:160px;width:880px;top:848px;text-align:center;font-size:14.6px;line-height:24px;color:var(--grey-light)}
.welcome-text p+p{margin-top:16px}
.btn-blue{left:506px;top:1045px;width:188px;height:51px;background:var(--blue);color:var(--white);font-size:21px;border-radius:3px;display:flex;align-items:center;justify-content:center;text-transform:uppercase}

/* commitment */
.planet{left:0;top:1150px;width:1200px;height:375px;background:linear-gradient(180deg,#dcecf9,#cfe6f6)}
.planet-title{left:0;width:1200px;top:1190px;color:var(--ink)}
.planet-text{left:80px;top:1280px;width:740px;font-size:16px;line-height:25px;color:var(--grey-light)}
.planet-photo{left:864px;top:1269px;width:257px;height:201px;border:2px solid #4a7fc1;background:radial-gradient(circle at 50% 55%,#5fbf3c 0,#2f8f2a 28%,#e9d2bf 46%,#f4f8fb 70%)}

/* newsletter */
.newsletter{left:0;top:1525px;width:1200px;height:243px;background:linear-gradient(180deg,#1b2f3d,#0f1d27 55%,#1f3443)}
.newsletter-title{left:0;width:1200px;top:1565px;color:var(--white)}
.field{top:1645px;height:46px;border:1px solid #c9d2da;color:#dfe6ec;font-size:16px;padding:0 12px;display:flex;align-items:center}
.field-name{left:181px;width:343px}
.field-email{left:533px;width:349px}
.btn-submit{left:893px;top:1645px;width:124px;height:46px;background:var(--white);color:var(--sky);font-size:22px;border-radius:3px;display:flex;align-items:center;justify-content:center;text-transform:uppercase}

/* news */
.news-title{left:0;width:1200px;top:1812px;color:var(--ink)}
.news-card{top:1896px;width:294px;text-align:center}
.news-photo{width:294px;height:156px}
.news-card h3{font-weight:400;font-size:18px;color:var(--ink);margin-top:20px}
.news-card.featured h3{color:var(--sky)}
.news-date{text-align:left;font-size:14px;color:var(--grey-light);margin-top:4px;display:flex;align-items:center;gap:8px}
.news-date svg{width:14px;height:14px}
.news-card p{font-size:14.5px;line-height:23px;color:var(--grey-light);margin-top:6px}
.news-more{font-size:14px;text-transform:uppercase;color:var(--ink)}
.news-card.featured .news-more{color:var(--blue)}

/* footer */
.footer-art{left:0;top:2190px;width:1200px;height:500px}
.contact-title{left:0;width:1200px;top:2428px;color:var(--white)}
.footer-nav{left:78px;top:2516px;display:flex;gap:40px;font-size:17px;color:var(--white)}
.social{left:952px;top:2520px;display:flex;gap:36px}
.social a{width:18px;height:18px;border-radius:50%;background:var(--white)}
.social a:first-child{background:var(--sky)}
.rule{left:78px;top:2555px;width:1044px;height:1px;background:#3a4d5e}
.contact-item{top:2594px;display:flex;align-items:center;gap:14px;color:var(--white);font-size:15px;line-height:21px}
.contact-icon{width:38px;height:38px;border-radius:50%;flex:none}
.contact-icon.outline{border:2px solid var(--sky)}
.contact-icon.solid{background:var(--white)}
.copyright{left:0;top:2688px;width:1200px;height:52px;background:var(--blue);color:var(--white);font-size:14px;display:flex;align-items:center;justify-content:center}
.copyright b{margin:0 4px}
</style>
</head>
<body>

<svg class="abs hero-art" viewBox="0 0 1200 760" aria-hidden="true">
  <defs>
    <linearGradient id="heroSky" x1="0" y1="0" x2="0" y2="1">
      <stop offset="0" stop-color="#2f4fa0"/>
      <stop offset=".32" stop-color="#5b6fb8"/>
      <stop offset=".5" stop-color="#e79a6b"/>
      <stop offset=".58" stop-color="#6c6f96"/>
      <stop offset="1" stop-color="#1b2c5c"/>
    </linearGradient>
  </defs>
  <path d="M0 0H1200V700Q600 630 0 700Z" fill="url(#heroSky)" role="img" aria-label="Photo of a white cruise ship sailing on the open sea at sunset"/>
  <path d="M0 716Q600 646 1200 716" fill="none" stroke="var(--sky)" stroke-width="8"/>
</svg>

<header>
  <a class="abs brand" href="#home"><span class="brand-mark"></span><span class="brand-name">KEELWISE</span></a>
  <nav class="abs main-nav">
    <a class="current" href="#home">Home</a><a href="#about">About</a><a href="#services">Services</a><a href="#mission">Mission</a><a href="#news">News</a><a href="#contact">Contact</a>
  </nav>
  <p class="abs tagline">Courageously leading our customers, partners, and ourselves to success by caring, thinking, and doing.</p>
  <a class="abs btn-light" href="#about">Read More</a>
</header>

<section id="about">
  <h1 class="abs heading welcome-title">Welcome to <span class="accent">Keelwise Software</span></h1>
  <div class="abs welcome-text">
    <p>We empower our Keelwise family to speak their mind and share their ideas, no matter how outside the box or crazy they are. We champion our team to challenge the status Quo and to set new standards to change the way business is done and to instill Optimism in everyone.</p>
    <p>Our senior leadership team's focus on the big picture and how our decisions impact our people, customers, partners and our planet sets us apart. Our clear vision on business standards and being accountable to our people ensures that our people live up to exceptional standards to drive us and out customers forward while being accountable for them, each other and our the environment.</p>
  </div>
  <a class="abs btn-blue" href="#mission">Read More</a>
</section>

<section id="mission">
  <div class="abs planet" role="img" aria-label="Soft light blue textured backdrop"></div>
  <h2 class="abs heading planet-title">Keelwise's Commitment to <span class="accent">our planet</span></h2>
  <p class="abs planet-text">Technology is one of the largest contributor of pollution on our planet. According to the National Waste Council, more than 4.6 million tonnes of e-waste ended up in landfills in 2000. Toxic chemicals in electronics products can leach into the land over time or are released into the atmosphere, impacting nearby communities and the environment. Our technology's benefit is that it works not only on the latest devices, it works on legacy systems allowing our clients to maintain older functioning technology longer keeping it our of land fills longer.</p>
  <div class="abs planet-photo" role="img" aria-label="Photo of cupped hands holding a small green globe with a butterfly"></div>
</section>

<section id="newsletter">
  <div class="abs newsletter" role="img" aria-label="Photo of dark ocean waves at night"></div>
  <h2 class="abs heading newsletter-title">Newsletter</h2>
  <div class="abs field field-name">Enter Name</div>
  <div class="abs field field-email">Enter E mail</div>
  <a class="abs btn-submit" href="#newsletter">Submit</a>
</section>

<section id="news">
  <h2 class="abs heading news-title">Latest <span class="accent">News</span></h2>

  <article class="abs news-card featured" style="left:77px">
    <div class="news-photo" role="img" aria-label="Photo of a white cruise ship on calm blue water" style="background:linear-gradient(180deg,#2f74c8,#7fb2e4 55%,#cfe2f4)"></div>
    <h3>Lorem Ipsum is simply dummy text</h3>
    <div class="news-date"><svg viewBox="0 0 14 14"><rect x="1" y="2" width="12" height="11" fill="none" stroke="#9a9a9a" stroke-width="1.5"/><line x1="1" y1="5.5" x2="13" y2="5.5" stroke="#9a9a9a" stroke-width="1.5"/></svg>10 August 2016</div>
    <p>Lorem Ipsum is simply dummy text of the printing and typesetting industry.</p>
    <a class="news-more" href="#news">Read More &raquo;</a>
  </article>

  <article class="abs news-card" style="left:453px">
    <div class="news-photo" role="img" aria-label="Photo collage of a compass, an airplane and a cruise ship in blue tones" style="background:linear-gradient(160deg,#a7cde6,#3f7fae 55%,#1d4f7a)"></div>
    <h3>Lorem Ipsum is simply dummy text</h3>
    <div class="news-date"><svg viewBox="0 0 14 14"><rect x="1" y="2" width="12" height="11" fill="none" stroke="#9a9a9a" stroke-width="1.5"/><line x1="1" y1="5.5" x2="13" y2="5.5" stroke="#9a9a9a" stroke-width="1.5"/></svg>10 August 2016</div>
    <p>Lorem Ipsum is simply dummy text of the printing and typesetting industry.</p>
    <a class="news-more" href="#news">Read More &raquo;</a>
  </article>

  <article class="abs news-card" style="left:829px">
    <div class="news-photo" role="img" aria-label="Photo of hands holding a planet Earth" style="background:radial-gradient(circle at 50% 45%,#3a6fb0 0,#6f9ccd 25%,#e2c6b0 48%,#ffffff 72%)"></div>
    <h3>Lorem Ipsum is simply dummy text</h3>
    <div class="news-date"><svg viewBox="0 0 14 14"><rect x="1" y="2" width="12" height="11" fill="none" stroke="#9a9a9a" stroke-width="1.5"/><line x1="1" y1="5.5" x2="13" y2="5.5" stroke="#9a9a9a" stroke-width="1.5"/></svg>10 August 2016</div>
    <p>Lorem Ipsum is simply dummy text of the printing and typesetting industry.</p>
    <a class="news-more" href="#news">Read More &raquo;</a>
  </article>
</section>

<footer id="contact">
  <svg class="abs footer-art" viewBox="0 2190 1200 500" aria-hidden="true">
    <defs>
      <linearGradient id="footerSea" x1="0" y1="0" x2="0" y2="1">
        <stop offset="0" stop-color="#1c2d3d"/>
        <stop offset=".5" stop-color="#243746"/>
        <stop offset="1" stop-color="#101c27"/>
      </linearGradient>
    </defs>
    <path d="M0 2260Q600 2340 1200 2260V2690H0Z" fill="url(#footerSea)" role="img" aria-label="Photo of a cruise ship at dusk, darkened"/>
    <path d="M0 2244Q600 2324 1200 2244" fill="none" stroke="var(--sky)" stroke-width="8"/>
  </svg>

  <h2 class="abs heading contact-title">Contact <span class="accent">Us</span></h2>
  <nav class="abs footer-nav">
    <a href="#home">Home</a><a href="#about">About</a><a href="#services">Services</a><a href="#mission">Mission</a><a href="#news">News</a><a href="#contact">Contact</a>
  </nav>
  <div class="abs social">
    <a href="#contact" aria-label="Social profile one"></a><a href="#contact" aria-label="Social profile two"></a><a href="#contact" aria-label="Social profile three"></a>
  </div>
  <div class="abs rule"></div>

  <div class="abs contact-item" style="left:75px">
    <svg class="contact-icon outline" viewBox="0 0 38 38"><path d="M19 9a6 6 0 0 1 6 6c0 5-6 12-6 12s-6-7-6-12a6 6 0 0 1 6-6z" fill="var(--sky)"/><circle cx="19" cy="15" r="2.2" fill="var(--footer)"/></svg>
    <span>123.Name,Street,Area,<br>Country ZIP Code</span>
  </div>
  <div class="abs contact-item" style="left:366px">
    <svg class="contact-icon solid" viewBox="0 0 38 38"><rect x="14" y="10" width="10" height="18" rx="2" fill="none" stroke="var(--blue)" stroke-width="2"/><circle cx="19" cy="24.5" r="1.2" fill="var(--blue)"/></svg>
    <span>781 204 6630</span>
  </div>
  <div class="abs contact-item" style="left:648px">
    <svg class="contact-icon solid" viewBox="0 0 38 38"><rect x="11" y="15" width="16" height="12" rx="1.5" fill="none" stroke="var(--blue)" stroke-width="2"/><rect x="14" y="10" width="10" height="6" fill="none" stroke="var(--blue)" stroke-width="2"/></svg>
    <span>781 204 6631</span>
  </div>
  <a class="abs contact-item" style="left:875px" href="mailto:keelwisesoftware@mail.com">
    <svg class="contact-icon solid" viewBox="0 0 38 38"><rect x="11" y="13" width="16" height="12" fill="none" stroke="var(--blue)" stroke-width="2"/><path d="M11 13l8 7 8-7" fill="none" stroke="var(--blue)" stroke-width="2"/></svg>
    <span>keelwisesoftware@mail.com</span>
  </a>

  <div class="abs copyright">&copy;<b>KEELWISE SOFTWARE</b> - 2016 All Right Reserved</div>
</footer>

</body>
</html>
```